Ferncrest Dental, LLC business card project

Business card to be designed with current logo.
Dental office- please keep design of card that looks clean and professional.
Please include the following info:
Ferncrest Dental, LLC
Dr. Lorna Pettigrew
2871 Marlowe Street
Bethlehem, PA 18093
610-555-0193
ferncrestdental.office@examplemail.test
Hello everyone-
Reason: Just got back from overseas- will look at all designs and provide feedback. Thank you!
Reason: Polling my friends for the final selection-
thank you to all those that participated- so many talented designers!

```html
<!DOCTYPE html>
<html lang="en">
<head>
<meta charset="utf-8">
<title>Ferncrest Dental, LLC — Business Card</title>
<link rel="stylesheet" href="https://fonts.googleapis.com/css2?family=Arimo:wght@400&display=swap">
<style>
  :root {
    --card-bg: #ffffff;
    --brand-green: #5cc40e;
    --name-ink: #1c1c1c;
    --detail-ink: #454545;
  }
  html, body {
    margin: 0;
    padding: 0;
    width: 1200px;
    height: 687px;
    overflow: hidden;
    background: var(--card-bg);
  }
  .business-card {
    position: relative;
    width: 1200px;
    height: 687px;
    background: var(--card-bg);
    font-family: "Arimo", Arial, sans-serif;
    font-weight: 400;
  }
  .brand {
    position: absolute;
    top: 104px;
    left: 0;
    width: 100%;
    display: flex;
    align-items: center;
    justify-content: center;
    gap: 22px;
  }
  .brand-dot {
    width: 58px;
    height: 58px;
    border-radius: 50%;
    background: var(--brand-green);
    flex: none;
  }
  .brand-name {
    font-size: 70px;
    line-height: 1;
    color: var(--brand-green);
    letter-spacing: -0.5px;
    white-space: nowrap;
  }
  .line {
    position: absolute;
    left: 0;
    width: 100%;
    margin: 0;
    text-align: center;
    line-height: 1;
    white-space: nowrap;
  }
  .doctor-name {
    top: 291px;
    font-size: 50px;
    color: var(--name-ink);
  }
  .address, .phone, .email {
    font-size: 41px;
    color: var(--detail-ink);
  }
  .address { top: 407px; }
  .phone   { top: 464px; }
  .email   { top: 549px; }
</style>
</head>
<body>
  <main class="business-card">
    <div class="brand">
      <span class="brand-dot" aria-hidden="true"></span>
      <span class="brand-name">Ferncrest Dental, LLC</span>
    </div>
    <p class="line doctor-name">Dr Lorna Pettigrew</p>
    <p class="line address">2871 Marlowe Street Bethlehem, PA 18093</p>
    <p class="line phone">610-555-0193</p>
    <p class="line email">ferncrestdental.office@examplemail.test</p>
  </main>
</body>
</html>
```